new business card, with new logo. Looking for full design

I would like to have a graphic designer/artist create a high standard, premium business logo and business card design that I can either use to print on my own or have printed through them as well. Also, would be nice if I could customize with new employee names and info afterwards. Also, though I don't have a logo, something that matches the theme here https://veridanstrategy.com/ as well as incorporates the letter "M" is what I am currently thinking. Thanks!

Target Market(s)

High end corporate executives

Industry/Entity Type

Economics

Contact Information for Business Card

Dr. Tomas Ruelle-Brandt
Principal Advisor
TRB@VeridanStrategy.com
other contact/website details from here: https://veridanstrategy.com/

Logo Text

Veridan Strategy Group

```html
<!DOCTYPE html>
<html lang="en">
<head>
<meta charset="utf-8">
<title>Veridan Strategy Group – Business Card</title>
<link rel="stylesheet" href="https://fonts.googleapis.com/css2?family=Cinzel:wght@500;600&family=Roboto:wght@400&display=swap">
<style>
  :root {
    --backdrop: #cfd3d4;
    --card-white: #f3f2ef;
    --rose: #c08f86;
    --rose-card: #cfa29d;
    --ink: #4a4c50;
    --white: #ffffff;
  }
  html, body {
    margin: 0;
    padding: 0;
    width: 1200px;
    height: 1050px;
    overflow: hidden;
    background: var(--backdrop);
  }
  .canvas {
    width: 1200px;
    height: 1050px;
    display: flex;
    flex-direction: column;
    align-items: center;
    justify-content: center;
    gap: 24px;
  }
  .card {
    width: 840px;
    height: 480px;
    box-sizing: border-box;
    position: relative;
    box-shadow: 0 2px 6px rgba(0,0,0,0.08);
  }
  .card--front {
    background: var(--card-white);
    border: 2px solid var(--rose);
  }
  .card--back {
    background: var(--rose-card);
    display: flex;
    align-items: center;
    justify-content: center;
  }
  .contact {
    position: absolute;
    left: 64px;
    top: 150px;
  }
  .contact__name {
    font-family: "Cinzel", serif;
    font-weight: 600;
    font-size: 26px;
    letter-spacing: 1px;
    color: var(--rose);
    margin: 0;
  }
  .contact__title {
    font-family: "Roboto", sans-serif;
    font-size: 21px;
    color: var(--ink);
    margin: 4px 0 22px;
  }
  .contact__list {
    list-style: none;
    margin: 0;
    padding: 0;
    font-family: "Roboto", sans-serif;
    font-size: 20px;
    color: var(--ink);
  }
  .contact__list li {
    display: flex;
    align-items: center;
    gap: 10px;
    margin-bottom: 8px;
  }
  .contact__icon {
    width: 18px;
    height: 18px;
    flex: none;
    fill: var(--rose);
  }
  .brand {
    display: flex;
    align-items: center;
    gap: 14px;
    font-family: "Cinzel", serif;
    font-weight: 600;
  }
  .brand__mark {
    flex: none;
  }
  .brand--front {
    position: absolute;
    right: 56px;
    top: 205px;
    color: var(--rose);
    font-size: 30px;
  }
  .brand--front .brand__mark {
    width: 26px;
    height: 26px;
    background: var(--rose);
  }
  .brand--back {
    color: var(--white);
    font-size: 46px;
  }
  .brand--back .brand__mark {
    width: 38px;
    height: 38px;
    background: var(--white);
  }
</style>
</head>
<body>
<main class="canvas">
  <section class="card card--front" aria-label="Card front">
    <div class="contact">
      <h1 class="contact__name">DR. TOMAS RUELLE-BRANDT</h1>
      <p class="contact__title">Principal Advisor</p>
      <ul class="contact__list">
        <li>
          <svg class="contact__icon" viewBox="0 0 24 24" aria-hidden="true"><path d="M6.6 10.8a15 15 0 0 0 6.6 6.6l2.2-2.2c.3-.3.7-.4 1-.2 1.1.4 2.3.6 3.6.6.6 0 1 .4 1 1V20c0 .6-.4 1-1 1A17 17 0 0 1 3 4c0-.6.4-1 1-1h3.5c.6 0 1 .4 1 1 0 1.3.2 2.5.6 3.6.1.3 0 .7-.2 1z"/></svg>
          555.014.2270
        </li>
        <li>
          <svg class="contact__icon" viewBox="0 0 24 24" aria-hidden="true"><path d="M2 5h20v14H2z M4 7v.5l8 5.5 8-5.5V7z" fill-rule="evenodd"/></svg>
          TRB@VeridanStrategy.com
        </li>
        <li>
          <svg class="contact__icon" viewBox="0 0 24 24" aria-hidden="true"><circle cx="12" cy="12" r="10"/></svg>
          www.veridanstrategy.com
        </li>
      </ul>
    </div>
    <div class="brand brand--front">
      <span class="brand__mark" aria-hidden="true"></span>
      <span class="brand__name">Veridan Strategy Group</span>
    </div>
  </section>

  <section class="card card--back" aria-label="Card back">
    <div class="brand brand--back">
      <span class="brand__mark" aria-hidden="true"></span>
      <span class="brand__name">Veridan Strategy Group</span>
    </div>
  </section>
</main>
</body>
</html>
```